Rug Cleaning Web Design Project

We need a web design for our cleaning company. We currently have a web page but are not happy with its design. We currently offer fine rug cleaning,upholstery cleaning, and residential and commercial carpet cleanning. We also offer water damage restoration. For our rug cleaning services we offer : Enzyme treatments for pet contamination and odor removal, application of stain protection that is designed for the fine textiles used in rug construction, application of treatments designed to prevent moth damage and pads designed to be used under rugs.Our current web site is harborfreshcare.example. We are intrested in a design with similar information to the web page of Velmora Rug Cleaners INC. We would like to use the colors that are present in our logo that will be uploaded with this description. We would also like this new page to be linked to our other address loomrinsepro.example. We would like the deign to be visually attractive but not "too busy".
Updates

Please include pictures of rugs, or people washing rugs if possible. We do not offer maid type cleaning services. We would not be interested in designs including pictures depicting that type service. Thanks for your hard work on this project.

Dana Whitlow

Industry/Entity Type

Residential

Requirements
Must have
• This page must be viewable on smart phones and tablets.

```html
<!DOCTYPE html>
<html lang="en">
<head>
<meta charset="utf-8">
<title>LoomRinse Pro – Harborfresh Cleaning</title>
<link rel="stylesheet" href="https://fonts.googleapis.com/css2?family=Signika:wght@400;600&family=Exo+2:ital,wght@1,600;1,700&family=Rokkitt:wght@400&family=Arimo:wght@400;700&display=swap">
<style>
:root{
  --bg-dark:#2b2b2b;
  --page:#ffffff;
  --blue:#1a6fb5;
  --blue-footer:#2a83cf;
  --orange:#f06a12;
  --ink:#111111;
  --text:#555555;
  --muted:#6a6a6a;
  --band:#f2f2f2;
  --card-border:#e2e2e2;
  --loc-bg:#e9e9e9;
}
*{box-sizing:border-box;margin:0;padding:0}
html,body{width:948px;height:1200px;overflow:hidden}
body{background:var(--bg-dark);position:relative;font-family:"Signika",sans-serif;color:var(--text)}
.rug-backdrop{position:absolute;left:0;top:0;width:948px;height:312px;
  background:linear-gradient(90deg,#8a3b22 0%,#b4552c 18%,#3d5b78 35%,#9c4a2a 55%,#c7743d 72%,#4b5d7a 88%,#8e3a24 100%)}
.floor-shadow{position:absolute;left:120px;top:1140px;width:710px;height:40px;border-radius:50%;
  background:radial-gradient(ellipse at center,rgba(0,0,0,.75) 0%,rgba(0,0,0,0) 70%)}
.page{position:absolute;left:111px;top:22px;width:726px;height:1088px;background:var(--page);border-radius:4px;box-shadow:0 0 12px rgba(0,0,0,.5)}
.abs{position:absolute}
.brand{left:19px;top:23px;display:flex;align-items:center;gap:13px}
.brand-dot{width:36px;height:36px;border-radius:50%;background:var(--blue)}
.brand-name{font-family:"Signika",sans-serif;font-weight:600;font-size:26px;color:var(--ink);line-height:1;letter-spacing:-.5px}
.brand-sub{font-family:"Signika",sans-serif;font-weight:600;font-size:8.5px;color:var(--ink);letter-spacing:2px;margin-top:3px}
.font-size{right:16px;top:17px;font-size:9px;color:var(--muted)}
.header-phone{right:22px;top:39px;font-family:"Exo 2",sans-serif;font-style:italic;font-weight:700;font-size:20px;color:var(--ink)}
.header-phone span{color:var(--orange)}
.header-mail{right:24px;top:63px;font-size:10.5px;color:#333}
.nav{left:15px;top:93px;width:696px;height:30px;background:var(--blue);display:flex}
.nav a{color:#fff;text-decoration:none;font-size:12px;line-height:30px;padding:0 14px;border-right:1px solid rgba(255,255,255,.7)}
.hero{left:15px;top:124px;width:696px;height:215px;display:flex}
.hero-photo{height:100%}
.caption{left:15px;top:295px;width:696px;height:44px;background:rgba(40,40,40,.72);color:#fff;font-family:"Rokkitt",serif;font-size:20px;line-height:44px;padding-left:15px}
.services{left:0;top:361px;width:726px;height:242px;background:var(--band)}
.service{position:absolute;top:0;width:163px}
.service h3{position:absolute;top:20px;font-size:11px;font-weight:600;color:var(--ink);white-space:nowrap}
.service-card{position:absolute;top:41px;left:0;width:163px;height:175px;background:#fff;border:1px solid var(--card-border)}
.service-img{position:absolute;left:8px;top:8px;width:147px;height:79px}
.service-card p{position:absolute;left:8px;top:93px;width:150px;font-size:9.5px;line-height:15px;color:#555}
.service-card .more{position:absolute;left:8px;top:153px;font-size:9px;color:#111;text-decoration:none}
.content{left:15px;top:630px;width:490px}
.content h2{font-family:"Exo 2",sans-serif;font-style:italic;font-weight:600;font-size:23px;color:var(--ink);letter-spacing:.3px;margin-bottom:8px}
.content p{font-size:11px;line-height:16.3px;color:var(--text);margin-bottom:16px}
.content .award{color:var(--orange)}
.content h2.second{margin-top:6px}
.location{left:530px;top:635px;width:181px;height:233px;background:var(--loc-bg)}
.location h4{background:var(--blue);color:#fff;font-family:"Exo 2",sans-serif;font-style:italic;font-weight:600;font-size:15px;height:29px;line-height:31px;padding-left:12px}
.loc-body{padding:10px 12px;font-size:11px;color:#555}
.loc-body .addr{font-style:italic;line-height:16.5px}
.loc-body .serve{font-family:"Rokkitt",serif;font-style:italic;font-size:10px}
.loc-body .label{font-weight:600;color:var(--ink);margin-top:16px}
.loc-body .phone{font-family:"Exo 2",sans-serif;font-style:italic;font-weight:700;font-size:19px;color:var(--orange);margin-top:-1px}
.loc-body .mail{font-style:italic}
.footer{position:absolute;left:104px;top:1042px;width:740px;height:60px;background:var(--blue-footer);color:#fff;font-size:9px;text-align:center;line-height:58px;box-shadow:0 2px 4px rgba(0,0,0,.3)}
.footer a{color:#fff;text-decoration:none}
</style>
</head>
<body>
<div class="rug-backdrop" role="img" aria-label="Photograph of colourful oriental rugs laid out at angles"></div>
<div class="floor-shadow"></div>

<main class="page">
  <div class="abs brand">
    <span class="brand-dot"></span>
    <div>
      <div class="brand-name">LoomRinse Pro</div>
      <div class="brand-sub">HARBORFRESH CLEANING, LLC</div>
    </div>
  </div>
  <div class="abs font-size">A+ | A–</div>
  <div class="abs header-phone"><span>(555)</span> 014-2277</div>
  <div class="abs header-mail">care@harborfreshcare.example</div>

  <nav class="abs nav">
    <a href="#">HOME</a><a href="#">ABOUT US</a><a href="#">RUG WASHING</a><a href="#">WATER DAMAGE</a><a href="#">CARPET CLEANING</a>
  </nav>

  <div class="abs hero">
    <div class="hero-photo" style="width:210px;background:linear-gradient(160deg,#eef2f6,#9aaecb 60%,#4d6690)" role="img" aria-label="Technician in cap and overalls beside water equipment"></div>
    <div class="hero-photo" style="width:247px;background:linear-gradient(180deg,#f6f4ef,#e6d8c5 60%,#cfae8e)" role="img" aria-label="Smiling family relaxing on a clean carpet"></div>
    <div class="hero-photo" style="width:239px;background:linear-gradient(180deg,#eceae6,#c9c4bb 55%,#4b4f57)" role="img" aria-label="Worker vacuuming an office carpet"></div>
  </div>
  <div class="abs caption">"Neque porro quisquam est qui dolorem ipsum quia dolor sit amet velit..."</div>

  <section class="abs services">
    <div class="service" style="left:15px">
      <h3>Rug Cleaning</h3>
      <div class="service-card">
        <div class="service-img" style="background:linear-gradient(135deg,#e8dcc4,#bfae90)" role="img" aria-label="Vacuum head on a beige rug"></div>
        <p>Lorem Ipsum is simply dummy text of the printing and type setting industry. Lorem..</p>
        <a class="more" href="#">Read More...</a>
      </div>
    </div>
    <div class="service" style="left:192px">
      <h3>Upholstery Cleaning</h3>
      <div class="service-card">
        <div class="service-img" style="background:linear-gradient(135deg,#5a5a58,#b9b1a0)" role="img" aria-label="Cleaning wand on an upholstered chair"></div>
        <p>Lorem Ipsum is simply dummy text of the printing and type setting industry. Lorem..</p>
        <a class="more" href="#">Read More...</a>
      </div>
    </div>
    <div class="service" style="left:370px">
      <h3 style="top:18px">Residential Carpet Cleanning</h3>
      <div class="service-card">
        <div class="service-img" style="background:linear-gradient(135deg,#a4452a,#d89a5a 55%,#7a3322)" role="img" aria-label="Vacuum on a patterned oriental carpet"></div>
        <p>Lorem Ipsum is simply dummy text of the printing and type setting industry. Lorem..</p>
        <a class="more" href="#">Read More...</a>
      </div>
    </div>
    <div class="service" style="left:547px">
      <h3 style="top:18px">Commercial Carpet Cleanning</h3>
      <div class="service-card">
        <div class="service-img" style="background:linear-gradient(135deg,#8a7a68,#d8d2c8 60%,#eeeae4)" role="img" aria-label="Worker cleaning a light commercial carpet"></div>
        <p>Lorem Ipsum is simply dummy text of the printing and type setting industry. Lorem..</p>
        <a class="more" href="#">Read More...</a>
      </div>
    </div>
  </section>

  <article class="abs content">
    <h2>WELCOME TO LOOMRINSE PRO</h2>
    <p>When it comes to cleaning carpet, oriental rugs, area rugs or furniture ~ any fabric from antique silk brocades to contemporary carpet fibers ~ our service is unparalled.</p>
    <p>Harborfresh Care &amp; Restoration is the recipient of the 2010 &amp; 2011 <span class="award">"BEST IN BUSINESS AWARD"</span> in Huntsville, Alabama for Water Damage Restoration and Carpet and Rug Cleaning.</p>
    <p>&nbsp;Please contact us for an extensive list of references.</p>
    <h2 class="second">FINE RUG WASHING</h2>
    <p>Oriental and Speciality Rugs differ greatly in their construction, dyeing methods and fiber content… and we understand these differences, assuring a safe and thorough in-plant cleaning of your speciality rugs.</p>
    <p>&nbsp;At Harborfresh, we strive to maximize cleaning without compromising delicate dyes or weaves and use a thorough, but gentle, total immersion method of cleaning for most rugs at $3.00 a square foot. Our team custom tailors the cleaning process to each rug depending on age, condition, fiber, construction and dyes…and that takes experience. Let our experience work for you and see why we are know as… "The LoomRinse Pro"</p>
  </article>

  <aside class="abs location">
    <h4>OUR LOCATION</h4>
    <div class="loc-body">
      <div class="addr">Harborfresh Care &amp; Restoration<br>48 Quarry Lane<br>Elmstead, AL&nbsp; 35700</div>
      <div class="serve">Serving Huntsville &amp; surrounding areas.</div>
      <div class="label" style="margin-top:20px">Phone:</div>
      <div class="phone">(555) 014-2277</div>
      <div class="label">Email:</div>
      <div class="mail">care@harborfreshcare.example</div>
    </div>
  </aside>
</main>

<footer class="footer">Copyright © 2012 LoomRinse Pro. All Rights Reserved &nbsp;|&nbsp; <a href="#">Site Map</a> | &nbsp;<a href="#">Privacy Policy</a> | &nbsp;<a href="#">Terms &amp; Conditions</a></footer>
</body>
</html>
```